Redesign of Current Wix Website - Event Production Company

Our website is www.trulvanshows.com and we need a redesign. We are full service event production company offering clients services including event management, graphics and content creation, vendor sourcing and management, contract review, audio visual production and venue selection. We would like our website to look more like an event management company, not just an audio visual company which it looks like now.
We want to look more like www.basquirelabs.com
Our Wix account is FILLED with logos, pictures and all the graphics you will need and we can assist with assets, categories and text.
On the Logo, I want to move away from "Halvindor Stage Production" and move to "Halvindor Stage Production" and I would like a redesigned logo with the same center element but a name change. I do have the art work files for the logo, vector and ai.

Target Market(s)

Event Planners and people that book event services. Assistants of CEOs. Marketing Directors. Gala Chairpersons and people in positions to purchase large scale event production

Industry/Entity Type

Event Management and Production - Corporate and Social

Coding

Coded - Design and coding required

Font styles to use
Other font styles liked:
• my logo is multicolor. look at it before you design

Colors
0054AA
0677BA
7BADD7
CADEEF
E8F1F8
6B429C
8869AF
B7A5CE
E3DAEB
F3F0F8

Requirements
Must have
• A clean professional look that shows the client who we are and what we do, and the full scope of what we do.
Nice to have
• www.basquirelabs.com ; https://themarbledrift.com/ look at these two website We are going after venues, planners end clients. Much like the on service page.

```html
<!DOCTYPE html>
<html lang="en">
<head>
<meta charset="utf-8">
<title>Halvindor Stage Production</title>
<link href="https://fonts.googleapis.com/css2?family=Bebas+Neue&family=Rubik:ital,wght@0,400;0,500;0,700;1,400&display=swap" rel="stylesheet">
<style>
:root{
  --blue:#0677BA;
  --blue-deep:#0054AA;
  --blue-soft:#7BADD7;
  --purple:#6B429C;
  --purple-soft:#8869AF;
  --navy:#1d2a44;
  --dark:#222222;
  --text:#4a4f5a;
  --white:#ffffff;
}
*{box-sizing:border-box;margin:0;padding:0}
html,body{width:1200px;height:4048px;overflow:hidden}
body{font-family:"Rubik",sans-serif;color:var(--text);background:var(--white);position:relative}
.display{font-family:"Bebas Neue",sans-serif;font-weight:400;letter-spacing:.5px}
section,header,footer{position:absolute;left:0;width:1200px}
.abs{position:absolute}
.btn{position:absolute;display:flex;align-items:center;justify-content:center;gap:8px;background:var(--blue);color:#fff;border-radius:24px;font:700 13px "Rubik",sans-serif;text-transform:uppercase;letter-spacing:.3px}
.btn svg{width:14px;height:14px}

/* top bar */
.topbar{top:0;height:47px;background:linear-gradient(#6a6a6a,#4e4e4e)}
.topbar .social{left:85px;top:14px;display:flex;gap:10px}
.topbar .social span{width:16px;height:16px;border:2px solid #fff;border-radius:3px;display:block}
.topbar .contact{right:85px;top:14px;display:flex;gap:30px;color:#fff;font:500 13px "Rubik",sans-serif}
.topbar .contact div{display:flex;align-items:center;gap:8px}

/* nav */
.nav{top:47px;height:115px;background:#fff}
.brand{left:80px;top:12px;width:180px;text-align:center}
.brand .mark{width:68px;height:68px;border-radius:50%;background:var(--purple);margin:0 auto}
.brand .name{font:500 13px/15px "Rubik",sans-serif;color:#555;letter-spacing:.5px;margin-top:5px;text-transform:uppercase}
.menu{left:292px;top:52px;display:flex;gap:34px;font:500 12px "Rubik",sans-serif;color:#333;text-transform:uppercase}
.menu .active{color:var(--blue)}
.nav .btn{left:956px;top:35px;width:158px;height:48px}

/* hero */
.hero{top:162px;height:560px;background:linear-gradient(100deg,#3a1d12 0%,#7a3c22 40%,#a86040 65%,#4a2418 100%)}
.hero .kicker{left:85px;top:170px;color:#fff;font-size:17px;letter-spacing:3px}
.hero h1{left:85px;top:200px;color:#fff;font-size:66px;line-height:69px}
.hero .btn{left:85px;top:367px;width:158px;height:48px}

/* about */
.about{top:722px;height:593px}
.about .label{left:85px;top:140px;color:var(--purple);font-size:14px;letter-spacing:3px}
.about h2{left:85px;top:158px;color:var(--navy);font-size:44px}
.about .rule{left:85px;top:222px;width:75px;height:2px;background:var(--blue)}
.about p{left:85px;top:252px;width:480px;font-size:14.5px;line-height:24.6px}
.about .btn{left:85px;top:399px;width:160px;height:48px}
.about .frame{left:612px;top:70px;width:502px;height:405px;border:1.5px solid var(--blue-soft)}
.about .photo{left:606px;top:78px;width:502px;height:402px;background:linear-gradient(135deg,#3b2a26,#8a5a3e 55%,#2a1d1a)}

/* services */
.services{top:1315px;height:1291px;background:var(--dark)}
.card{position:absolute;width:331px;height:540px}
.card .img{height:249px}
.card h3{margin-top:40px;color:#fff;font-size:20px}
.card p{margin-top:10px;color:#e6e6e6;font-size:14.5px;line-height:24.6px}
.card .more{position:absolute;left:0;display:inline-flex;align-items:center;gap:6px;color:var(--blue-soft);font:700 12.5px "Rubik",sans-serif;text-transform:uppercase;border-bottom:1.5px solid var(--blue-soft);padding-bottom:3px}
.intro{left:85px;top:94px;width:331px;height:530px;background:linear-gradient(160deg,#6B429C 0%,#8869AF 30%,#0677BA 65%,#7BADD7 100%);display:flex;align-items:center;justify-content:center}
.intro h2{color:#fff;font-size:46px}

/* testimonial */
.testimonial{top:2606px;height:663px}
.testimonial .photo{left:85px;top:114px;width:480px;height:450px;background:linear-gradient(#1e1e1e,#8a8a8a 50%,#2c2c2c)}
.testimonial .quote{left:594px;top:127px}
.testimonial blockquote{left:624px;top:178px;width:470px;font:italic 400 24px/41px "Rubik",sans-serif;color:#556079}
.testimonial cite{left:624px;top:538px;font:700 16px "Rubik",sans-serif;color:var(--navy);font-style:normal}

/* cta */
.cta{top:3269px;height:286px;background:linear-gradient(100deg,#B7A5CE 0%,#8869AF 35%,#7BADD7 75%,#CADEEF 100%)}
.cta h2{left:0;width:1200px;top:65px;text-align:center;color:#fff;font-size:48px;line-height:54px}
.cta .btn{left:488px;top:182px;width:224px;height:46px;background:var(--blue-deep)}

/* footer */
.footer{top:3555px;height:493px;background:var(--dark);color:#fff}
.footer .logo{left:85px;top:52px;width:330px;text-align:center}
.footer .logo .mark{width:108px;height:108px;border-radius:50%;background:var(--purple);margin:0 auto}
.footer .logo .name{font:500 22px "Rubik",sans-serif;letter-spacing:1px;margin-top:12px;text-transform:uppercase}
.footer .about-text{left:85px;top:243px;width:330px;text-align:center;font-size:14.5px;line-height:24.6px}
.col{position:absolute;top:133px}
.col h4{font-size:17px;letter-spacing:1px}
.col .bar{width:30px;height:2px;background:#fff;margin-top:10px}
.col ul{list-style:none;margin-top:20px}
.col li{font-size:14.5px;height:36px;display:flex;align-items:center;gap:10px}
.col .icons{display:flex;gap:14px;margin-top:18px}
.col .icons span{width:18px;height:18px;border:2.5px solid #fff;border-radius:3px}
.footer .bottom{left:85px;top:426px;width:1029px;display:flex;align-items:center;gap:8px;font-size:13px}
.footer .bottom .line{flex:1;height:1px;background:#666}
.footer .bottom b{color:var(--blue-soft);font-weight:500}
</style>
</head>
<body>

<header class="topbar">
  <div class="abs social"><span></span><span></span><span></span></div>
  <div class="abs contact">
    <div><svg width="14" height="11" viewBox="0 0 14 11"><rect width="14" height="11" rx="1" fill="#7BADD7"/><path d="M0 1l7 5 7-5" stroke="#fff" stroke-width="1.2" fill="none"/></svg>dana@trvshows.com</div>
    <div><svg width="13" height="13" viewBox="0 0 24 24"><path fill="#7BADD7" d="M6.6 10.8a15 15 0 006.6 6.6l2.2-2.2a1 1 0 011-.25 11.4 11.4 0 003.6.6 1 1 0 011 1V20a1 1 0 01-1 1A17 17 0 013 4a1 1 0 011-1h3.5a1 1 0 011 1c0 1.25.2 2.45.6 3.6a1 1 0 01-.25 1z"/></svg>(555) 310-2748</div>
  </div>
</header>

<header class="nav">
  <div class="abs brand"><div class="mark"></div><div class="name">Halvindor Stage<br>Production</div></div>
  <nav class="abs menu">
    <span class="active">Who we are</span><span>What we do</span><span>Event Production</span><span>Content Creation</span><span>HSP Social Media</span>
  </nav>
  <a class="btn">Get a quote <svg viewBox="0 0 16 16"><circle cx="8" cy="8" r="8" fill="#fff"/><path d="M6 4.5L9.5 8 6 11.5" stroke="#0677BA" stroke-width="2" fill="none"/></svg></a>
</header>

<section class="hero" role="img" aria-label="Ballroom set for a reception with a lit head table and monogram projection">
  <div class="abs kicker display">We are dedicated to helping you bring</div>
  <h1 class="abs display">Your vision to life<br>through our expert</h1>
  <a class="btn">Get a quote <svg viewBox="0 0 16 16"><circle cx="8" cy="8" r="8" fill="#fff"/><path d="M6 4.5L9.5 8 6 11.5" stroke="#0677BA" stroke-width="2" fill="none"/></svg></a>
</section>

<section class="about">
  <div class="abs label display">About</div>
  <h2 class="abs display">Halvindor Stage Production</h2>
  <div class="abs rule"></div>
  <p class="abs">Welcome to Halvindor Stage Productions (HSP), your go-to source for professional Film and Content Creation Services. Our team of experienced directors, camera crew, and lighting crew are dedicated to helping our clients bring their vision to life through high-quality video production.</p>
  <a class="btn">Learn more <svg viewBox="0 0 16 16"><circle cx="8" cy="8" r="8" fill="#fff"/><path d="M6 4.5L9.5 8 6 11.5" stroke="#0677BA" stroke-width="2" fill="none"/></svg></a>
  <div class="abs frame"></div>
  <div class="abs photo" role="img" aria-label="Production crew at a control desk overlooking a seated audience"></div>
</section>

<section class="services">
  <div class="abs intro"><h2 class="display">What we do</h2></div>

  <div class="card" style="left:434px;top:94px">
    <div class="img" role="img" aria-label="Conference stage with blue lighting and projection screens" style="background:linear-gradient(#1c2a8a,#3550c8 50%,#5a2a4a)"></div>
    <h3 class="display">Event Production</h3>
    <p>Halvindor Stage Production LLC is a full-service event production company that specializes in creating amazing experiences for our clients. We are dedicated to helping you bring your vision to life through our expert audio visual, planning, logistics, lighting, staging, and design services.</p>
    <span class="more" style="top:517px">Learn more <svg width="13" height="13" viewBox="0 0 16 16"><circle cx="8" cy="8" r="8" fill="#7BADD7"/><path d="M6 4.5L9.5 8 6 11.5" stroke="#222" stroke-width="2" fill="none"/></svg></span>
  </div>

  <div class="card" style="left:783px;top:94px">
    <div class="img" role="img" aria-label="Camera operator checking a rig monitor" style="background:linear-gradient(135deg,#2a2420,#6b4a30 55%,#1a1614)"></div>
    <h3 class="display">Film &amp; Videography</h3>
    <p>Welcome to Halvindor Stage Productions (HSP), your go-to source for professional Film and Content Creation Services. Our team of experienced directors, camera crew, and lighting crew are dedicated to helping our clients bring their vision to life through high-quality video production.</p>
    <span class="more" style="top:517px">Learn more <svg width="13" height="13" viewBox="0 0 16 16"><circle cx="8" cy="8" r="8" fill="#7BADD7"/><path d="M6 4.5L9.5 8 6 11.5" stroke="#222" stroke-width="2" fill="none"/></svg></span>
  </div>

  <div class="card" style="left:85px;top:681px">
    <div class="img" role="img" aria-label="Conference hall with rows of chairs and laptops on a tech table" style="background:linear-gradient(#7a5a48,#3a2c2a 55%,#1f2a6a)"></div>
    <h3 class="display">Meeting, Conference &amp; Gala Planning</h3>
    <p style="margin-top:26px">Halvindor Stage Production works with local and national clients, consulting on several aspects of the meeting, conference and gala planning process.</p>
    <p style="margin-top:8px">Finding a venue, creating a technical design and layout, contracting with several vendors</p>
    <span class="more" style="top:517px">Learn more <svg width="13" height="13" viewBox="0 0 16 16"><circle cx="8" cy="8" r="8" fill="#7BADD7"/><path d="M6 4.5L9.5 8 6 11.5" stroke="#222" stroke-width="2" fill="none"/></svg></span>
  </div>

  <div class="card" style="left:434px;top:681px">
    <div class="img" role="img" aria-label="Reception room with floral centerpiece and wedding cake" style="background:linear-gradient(#e8e4dc,#d8c4a8 60%,#b89a78)"></div>
    <h3 class="display">Hyrbid Event Design</h3>
    <p>Welcome to Halvindor Stage Productions, your premier provider of Hybrid Event Services that expertly integrate complex audio visual systems with current virtual meeting technology. Our innovative approach combines the best of both worlds, allowing you to host events that seamlessly blend</p>
    <span class="more" style="top:517px">Learn more <svg width="13" height="13" viewBox="0 0 16 16"><circle cx="8" cy="8" r="8" fill="#7BADD7"/><path d="M6 4.5L9.5 8 6 11.5" stroke="#222" stroke-width="2" fill="none"/></svg></span>
  </div>

  <div class="card" style="left:783px;top:681px">
    <div class="img" role="img" aria-label="Technician at an editing console with monitors" style="background:linear-gradient(135deg,#2a3a6a,#6a7aa8 50%,#1a1a22)"></div>
    <h3 class="display">Audio Visual Production</h3>
    <p>Audio Visual is the foundation of any successful event. HSP has over 20 years of expertise in Audio Visual contracting, staffing and equipment allocation.</p>
    <p style="margin-top:8px">Our specialty is putting together custom designed AV solution to fit your media, venue</p>
    <span class="more" style="top:517px">Learn more <svg width="13" height="13" viewBox="0 0 16 16"><circle cx="8" cy="8" r="8" fill="#7BADD7"/><path d="M6 4.5L9.5 8 6 11.5" stroke="#222" stroke-width="2" fill="none"/></svg></span>
  </div>
</section>

<section class="testimonial">
  <div class="abs photo" role="img" aria-label="Black and white ballroom stage with chandelier and uplit speaker stands"></div>
  <svg class="abs quote" width="64" height="46" viewBox="0 0 64 46"><path fill="#0677BA" d="M0 46V26C0 10 8 2 24 0v8c-8 2-12 7-12 14h12v24zM36 46V26C36 10 44 2 60 0v8c-8 2-12 7-12 14h12v24z"/></svg>
  <blockquote class="abs">I wanted to thank you and your team for doing an excellent job with the set up for the red carpet award night. The stage looked amazing and your efforts helped us make the event memorable. We truly appreciate your professionalism, quick turnaround and quality of work… job well done!!</blockquote>
  <cite class="abs">- CORVANE CONSULTING</cite>
</section>

<section class="cta">
  <h2 class="abs display">Let's connect<br>for your next event</h2>
  <a class="btn">Get a quote now <svg viewBox="0 0 16 16"><circle cx="8" cy="8" r="8" fill="#fff"/><path d="M6 4.5L9.5 8 6 11.5" stroke="#0054AA" stroke-width="2" fill="none"/></svg></a>
</section>

<footer class="footer">
  <div class="abs logo"><div class="mark"></div><div class="name">Halvindor Stage Production</div></div>
  <p class="abs about-text">Welcome to Halvindor Stage Productions (HSP), your go-to source for professional Film and Content Creation Services. Our team of experienced director</p>
  <div class="col" style="left:493px">
    <h4 class="display">Quick links</h4><div class="bar"></div>
    <ul><li>Who we are</li><li>What we do</li><li>Event Production</li><li>Content Creation</li><li>HSP Social Media</li></ul>
  </div>
  <div class="col" style="left:707px">
    <h4 class="display">Contact info</h4><div class="bar"></div>
    <ul>
      <li><svg width="15" height="15" viewBox="0 0 24 24"><path fill="#fff" d="M6.6 10.8a15 15 0 006.6 6.6l2.2-2.2a1 1 0 011-.25 11.4 11.4 0 003.6.6 1 1 0 011 1V20a1 1 0 01-1 1A17 17 0 013 4a1 1 0 011-1h3.5a1 1 0 011 1c0 1.25.2 2.45.6 3.6a1 1 0 01-.25 1z"/></svg>(555) 310-2748</li>
      <li><svg width="15" height="12" viewBox="0 0 14 11"><rect width="14" height="11" rx="1" fill="#fff"/><path d="M0 1l7 5 7-5" stroke="#222" stroke-width="1.2" fill="none"/></svg>dana@trvshows.com</li>
    </ul>
  </div>
  <div class="col" style="left:957px">
    <h4 class="display">Get in touch</h4><div class="bar"></div>
    <div class="icons"><span></span><span></span><span></span></div>
  </div>
  <div class="abs bottom"><span>© 2025 <b>Halvindor Stage Production</b>. All right reserved</span><span class="line"></span><span>January 27, 2025. Layout_4</span></div>
</footer>

</body>
</html>
```